WordPress Plugin Cover Image for ScriptHarbor

We need a new cover image for our WordPress plugin Mosaic Brick Pane Album, you can see it here: http://scriptharbor.example/item/mosaic-brick-pane-album-for-wordpress/7403628 the cover image is: http://2.cdn.quorvel.example/files/52917340/MBP_1.jpg this is a plugin to make galleries with a new concept grid, where images are tiled like a puzzle, instead of the usual multi-columns or multi-rows layouts. See details here: http://belstrandia.example/mosaic-brick-album-demo

The cover image has to communicate few key features of the plugin and it should show an example of the galleries the user can create.

The main feature is the completely new and unique grid system.

You are free and encouraged to use new colors and fonts, I like high contrast schemes like dark grey and fluo colors (orange, lime, cyan).

This is a list of other cover images I like the style:
http://0.cdn.quorvel.example/files/61204758/01_Preview.jpg
http://3.cdn.quorvel.example/files/48830512/Banner.png
http://1.cdn.quorvel.example/files/27749065/image-preview.png
http://0.cdn.quorvel.example/files/93156207/previewv12.jpg
http://1.cdn.quorvel.example/files/16628473/preview.jpg

```html
<!DOCTYPE html>
<html lang="en">
<head>
<meta charset="utf-8">
<title>Mosaic Brick Pane Album — Cover</title>
<link rel="stylesheet" href="https://fonts.googleapis.com/css2?family=Open+Sans:wght@300;400;700;800&display=swap">
<style>
  :root {
    --bg-center: #3a3a3a;
    --bg-edge: #161616;
    --ink: #ffffff;
    --accent: #3be08f;
    --band-cyan: #1ec3e6;
    --band-green: #4fd666;
    --band-lime: #d9ea2b;
    --band-orange: #f47a20;
    --band-pink: #ee2b6c;
    --bezel: #0d0d0d;
    --silver-a: #e8e8ea;
    --silver-b: #b9bbc0;
    --device-white: #f5f5f5;
    --icon: #e6e6e6;
  }
  * { margin: 0; padding: 0; box-sizing: border-box; }
  html, body { width: 1200px; height: 610px; overflow: hidden; background: var(--bg-edge); }
  .cover {
    position: relative; width: 1200px; height: 610px; overflow: hidden;
    background: radial-gradient(ellipse 70% 80% at 45% 50%, var(--bg-center), var(--bg-edge));
    font-family: "Open Sans", Arial, sans-serif; color: var(--ink);
  }
  .color-band { position: absolute; top: 0; left: 0; width: 100%; height: 12px; display: flex; }
  .color-band span { flex: 1; }
  .color-band .cyan { background: var(--band-cyan); }
  .color-band .green { background: var(--band-green); }
  .color-band .lime { background: var(--band-lime); }
  .color-band .orange { background: var(--band-orange); }
  .color-band .pink { background: var(--band-pink); }

  .title { position: absolute; left: 77px; top: 62px; text-align: center; }
  .title-main { font-weight: 800; font-size: 62px; line-height: 1; letter-spacing: 1px; }
  .title-sub { font-weight: 300; font-size: 58px; line-height: 1.05; letter-spacing: 9px; margin-top: 4px; }

  .features { position: absolute; left: 77px; top: 226px; list-style: none; }
  .features li { font-size: 27px; line-height: 55px; font-weight: 400; white-space: nowrap; }
  .features strong { color: var(--accent); font-weight: 700; }

  .device { position: absolute; }
  .screen { position: absolute; overflow: hidden; background: #222; }
  .tile { position: absolute; }

  .desktop { left: 722px; top: 193px; width: 454px; height: 340px; }
  .desktop .frame { position: absolute; left: 0; top: 0; width: 454px; height: 288px; background: var(--bezel); border-radius: 10px 10px 0 0; }
  .desktop .screen { left: 16px; top: 12px; width: 422px; height: 266px; }
  .desktop .chin { position: absolute; left: 0; top: 288px; width: 454px; height: 38px; background: linear-gradient(var(--silver-a), var(--silver-b)); border-radius: 0 0 10px 10px; }
  .desktop .chin::after { content: ""; position: absolute; left: 219px; top: 12px; width: 16px; height: 16px; border-radius: 50%; background: #9a9ca1; }
  .desktop .stand { position: absolute; left: 175px; top: 326px; width: 104px; height: 14px; background: linear-gradient(#a5a7ac, #d4d5d8); }

  .tablet { left: 680px; top: 264px; width: 182px; height: 270px; background: var(--device-white); border-radius: 16px; box-shadow: 0 4px 12px rgba(0,0,0,.45); }
  .tablet .screen { left: 12px; top: 24px; width: 158px; height: 222px; }
  .tablet .home { position: absolute; left: 84px; top: 252px; width: 14px; height: 14px; border-radius: 50%; border: 1px solid #c9c9c9; }

  .phone { left: 814px; top: 362px; width: 82px; height: 166px; background: var(--device-white); border-radius: 12px; box-shadow: 0 4px 12px rgba(0,0,0,.45); }
  .phone .screen { left: 6px; top: 22px; width: 70px; height: 120px; }
  .phone .home { position: absolute; left: 34px; top: 148px; width: 13px; height: 13px; border-radius: 50%; border: 1px solid #c9c9c9; }

  .platforms { position: absolute; left: 752px; top: 556px; display: flex; gap: 30px; }
  .platforms span { width: 32px; height: 32px; border-radius: 50%; background: var(--icon); opacity: .9; }
</style>
</head>
<body>
<main class="cover">
  <div class="color-band"><span class="cyan"></span><span class="green"></span><span class="lime"></span><span class="orange"></span><span class="pink"></span></div>

  <header class="title">
    <div class="title-main">MOSAIC BRICK</div>
    <div class="title-sub">ALBUM</div>
  </header>

  <ul class="features">
    <li><strong>&gt; Complex grids</strong> (no rows, squares or columns)</li>
    <li><strong>&gt; Responsive</strong> / Mobile layout</li>
    <li><strong>&gt; 5 lightboxes</strong> included</li>
    <li><strong>&gt; Custom links</strong> on images</li>
    <li><strong>&gt; Advanced admin</strong> UI</li>
    <li><strong>&gt; Fine tuning</strong> on captions</li>
  </ul>

  <div class="device desktop">
    <div class="frame">
      <div class="screen" role="img" aria-label="Tiled gallery of city architecture and bird photographs">
        <div class="tile" style="left:0;top:0;width:132px;height:92px;background:linear-gradient(#6b3a2a,#2e2420)"></div>
        <div class="tile" style="left:134px;top:0;width:288px;height:130px;background:linear-gradient(#cfd6d9,#8d9591)"></div>
        <div class="tile" style="left:0;top:94px;width:90px;height:172px;background:linear-gradient(#7e7a74,#3b3a38)"></div>
        <div class="tile" style="left:92px;top:94px;width:40px;height:80px;background:#5c5f63"></div>
        <div class="tile" style="left:134px;top:132px;width:140px;height:134px;background:linear-gradient(#b7c2cc,#6d737a)"></div>
        <div class="tile" style="left:92px;top:176px;width:40px;height:90px;background:#2f3134"></div>
        <div class="tile" style="left:276px;top:132px;width:146px;height:134px;background:linear-gradient(#9a9c9e,#4a4c4f)"></div>
      </div>
    </div>
    <div class="chin"></div>
    <div class="stand"></div>
  </div>

  <div class="device tablet">
    <div class="screen" role="img" aria-label="Tiled gallery of street and building photographs">
      <div class="tile" style="left:0;top:0;width:50px;height:62px;background:#4a5058"></div>
      <div class="tile" style="left:52px;top:0;width:106px;height:62px;background:linear-gradient(#c9cfd3,#9aa0a3)"></div>
      <div class="tile" style="left:0;top:64px;width:106px;height:70px;background:linear-gradient(#dfe4e8,#a7adb0)"></div>
      <div class="tile" style="left:108px;top:64px;width:50px;height:70px;background:#6b6560"></div>
      <div class="tile" style="left:0;top:136px;width:40px;height:86px;background:#3f4a60"></div>
      <div class="tile" style="left:42px;top:136px;width:58px;height:40px;background:#8a5a3c"></div>
      <div class="tile" style="left:42px;top:178px;width:58px;height:44px;background:#5a5d62"></div>
      <div class="tile" style="left:102px;top:136px;width:56px;height:86px;background:linear-gradient(#b0b4b7,#707478)"></div>
    </div>
    <div class="home"></div>
  </div>

  <div class="device phone">
    <div class="screen" role="img" aria-label="Tiled gallery of photographs on a phone">
      <div class="tile" style="left:0;top:0;width:70px;height:40px;background:linear-gradient(#d4d9dc,#9ca2a5)"></div>
      <div class="tile" style="left:0;top:42px;width:34px;height:78px;background:#8f9396"></div>
      <div class="tile" style="left:36px;top:42px;width:34px;height:36px;background:#4b5057"></div>
      <div class="tile" style="left:36px;top:80px;width:34px;height:40px;background:#6d6a66"></div>
    </div>
    <div class="home"></div>
  </div>

  <div class="platforms" aria-label="Supported browsers and platforms">
    <span></span><span></span><span></span><span></span><span></span><span></span><span></span>
  </div>
</main>
</body>
</html>
```